Kelo8Ventra Roadmap for developing engineer 3D-BIM-projects over a longer period of time

We need functional and scalable PowerPoint templates with four main slides. The design should be carried out in the context of the enclosed documents; or at least in this sense.
As engineers, we develop projects over a longer period of time. To visualize topics along the way (downside timeline) and goals (upside timeline) for our customers (and for us), we need an overview for the project management in sort of a roadmap.
Our design requirements are simplicity, clarity and accuracy. These are also the service requirements for our customers.
As always, it's urgent. Our goal is to select the design by Wednesday November 10th and make any adjustments with the winner by Friday November 12th.

Target Market(s)

Architects, Engineers, World Heritage; 3D-Modelling, BIM Building Information Modeling

Industry/Entity Type

World Heritage Buildings and Objects

Requirements
Must have
• simplicity, logic, elegant (see the attached documents)
Nice to have
• see the attached documents

```html
<!DOCTYPE html>
<html lang="en">
<head>
<meta charset="utf-8">
<title>Kelo8Ventra Roadmap Templates</title>
<link href="https://fonts.googleapis.com/css2?family=Roboto:ital,wght@0,300;0,400;0,500;0,700;1,400&display=swap" rel="stylesheet">
<style>
:root{
  --page:#c8c8c8;
  --paper:#ffffff;
  --band:#f0f0f1;
  --ink:#111111;
  --muted:#555555;
  --red:#ee1c1c;
  --blue:#1d5aa6;
  --gold:#c9a45a;
  --bar:#7b7b7b;
  --dot:#d6d6d6;
  --rule:#dcdcdc;
}
*{box-sizing:border-box;margin:0;padding:0}
html,body{width:797px;height:1200px;overflow:hidden;background:var(--page)}
body{position:relative;font-family:"Roboto",sans-serif;color:var(--ink)}
.slide{position:absolute;width:345px;height:259px;background:var(--paper);overflow:hidden}
.abs{position:absolute}

/* title slides */
.photo{position:absolute;right:0;top:0;height:100%;width:190px;
  background:linear-gradient(100deg,rgba(255,255,255,1) 0%,rgba(226,232,238,.8) 30%,#8fa3b6 55%,#3c5670 78%,#0f2235 100%)}
.photo.light{width:210px;background:linear-gradient(100deg,#fff 0%,#f1f3f5 40%,#dfe3e8 75%,#d2d7dd 100%)}
.brand{position:absolute;left:24px;top:62px;display:flex;align-items:center;gap:5px}
.brand-square{width:9px;height:9px;background:var(--red)}
.brand-name{font-weight:700;font-size:21px;color:var(--blue);letter-spacing:-.3px}
.gold-rule{position:absolute;height:1px;background:var(--gold)}
.project-title{position:absolute;left:24px;top:130px;font-size:15px;font-weight:500}
.project-lead{position:absolute;left:25px;top:153px;font-size:5.6px;line-height:8.8px;color:var(--muted);width:140px}

/* roadmap header */
.head-title{position:absolute;left:21px;font-size:13px;font-weight:700}
.head-year{position:absolute;right:20px;font-size:13.5px;font-weight:300}
.band{position:absolute;left:0;width:100%;background:var(--band)}
.play-mark{position:absolute;left:22px;width:0;height:0;border-top:4px solid transparent;border-bottom:4px solid transparent;border-left:8px solid #cfcfcf}

/* timeline */
.chev{position:absolute;width:8px;height:16px}
.track{position:absolute;left:32px;width:280px;height:13px;background:#000}
.track .active{position:absolute;left:21px;width:40px;top:0;height:100%;background:var(--red)}
.track .start{position:absolute;left:12px;top:3.5px;border-top:3px solid transparent;border-bottom:3px solid transparent;border-left:5px solid #fff}
.month{position:absolute;top:0;line-height:13px;font-size:5.8px;font-weight:500;color:#fff;transform:translateX(-50%)}
.dot{position:absolute;top:-6px;width:6px;height:6px;border-radius:50%;background:var(--dot);transform:translateX(-50%)}
.ring{position:absolute;top:-8px;width:11px;height:11px;border-radius:50%;background:#fff;border:1px solid #000;transform:translateX(-50%)}
.ring::after{content:"";position:absolute;left:2px;top:2px;width:5px;height:5px;border-radius:50%;background:var(--dot)}

/* gantt */
.milestone{position:absolute;font-size:5.8px;font-weight:500;transform:translateX(-50%);white-space:nowrap}
.stem{position:absolute;width:.7px;background:#000}
.task-label{position:absolute;left:21px;font-size:5.6px;font-style:italic;color:var(--muted)}
.task-line{position:absolute;left:40px;right:32px;height:.5px;background:var(--rule)}
.task-bar{position:absolute;height:11px;line-height:11px;font-size:5.4px;color:#fff;text-align:center;background:var(--bar)}
.task-bar.current{background:var(--red)}

/* detail */
.topic{position:absolute;left:0;width:100%;text-align:center;font-size:8.4px;font-weight:700}
.caret{position:absolute;left:50%;width:18px;height:6px;transform:translateX(-50%)}
.card{position:absolute;left:56px;width:231px;background:#fff}
.para{position:absolute;left:15px;width:205px;font-size:5.6px;line-height:9px;color:#333}
.bullets{position:absolute;left:18px;list-style:none}
.bullets li{position:relative;padding-left:8px;font-size:5.6px;height:15px;line-height:6px;color:#222}
.bullets li::before{content:"";position:absolute;left:0;top:1.6px;width:3px;height:3px;border-radius:50%;background:#000}

/* thanks */
.thanks-title{position:absolute;left:30px;top:56px;font-size:26.5px;font-weight:500}
.contact{position:absolute;left:30px;display:flex;align-items:center;gap:4px;font-size:5.6px;font-weight:300;color:#555}
.contact-icon{width:16px;height:16px;border-radius:50%;background:#000;display:flex;align-items:center;justify-content:center}
</style>
</head>
<body>

<!-- Title slide A -->
<section class="slide" style="left:44px;top:55px">
  <div class="photo" role="img" aria-label="Photo of a glass high-rise facade seen from below"></div>
  <div class="brand"><span class="brand-square"></span><span class="brand-name">Kelo8Ventra</span></div>
  <div class="gold-rule" style="left:24px;top:113px;width:142px"></div>
  <h1 class="project-title">Projectname</h1>
  <p class="project-lead">Maecenas sed diam dget risusu ipsum dolor sit amet, consectetur adipiscing elit ds. Nam suscipit</p>
</section>

<!-- Title slide B -->
<section class="slide" style="left:408px;top:55px">
  <div class="photo" role="img" aria-label="Photo of a glass high-rise facade seen from below"></div>
  <div class="brand"><span class="brand-square"></span><span class="brand-name">Tamu5Ventra</span></div>
  <div class="gold-rule" style="left:24px;top:113px;width:142px"></div>
  <h1 class="project-title">Projectname</h1>
  <p class="project-lead">Maecenas sed diam dget risusu ipsum dolor sit amet, consectetur adipiscing elit ds. Nam suscipit</p>
</section>

<!-- Roadmap overview -->
<section class="slide" style="left:44px;top:330px">
  <h2 class="head-title" style="top:18px">Roadmap</h2>
  <div class="head-year" style="top:17px">2021</div>
  <div class="band" style="top:46px;height:198px"></div>

  <div class="milestone" style="left:283.5px;top:50px">Roadmap 2022</div>
  <div class="milestone" style="left:263px;top:67px">Mock-up</div>
  <div class="milestone" style="left:163px;top:83px">Datenbanken</div>
  <div class="milestone" style="left:124px;top:97px">Kick-off</div>
  <div class="stem" style="left:283.2px;top:58px;height:59px"></div>
  <div class="stem" style="left:262.7px;top:75px;height:42px"></div>
  <div class="stem" style="left:162.7px;top:91px;height:26px"></div>
  <div class="stem" style="left:123.7px;top:105px;height:12px"></div>

  <svg class="chev" style="left:21px;top:123.5px" viewBox="0 0 8 16"><polyline points="6.5,1 2,8 6.5,15" fill="none" stroke="#000" stroke-width="2.4"/></svg>
  <svg class="chev" style="left:316px;top:123.5px" viewBox="0 0 8 16"><polyline points="1.5,1 6,8 1.5,15" fill="none" stroke="#000" stroke-width="2.4"/></svg>
  <div class="track" style="top:125px">
    <span class="start"></span>
    <span class="month" style="left:31px">JAN</span><span class="month" style="left:72px">MAR</span><span class="month" style="left:92px">APR</span><span class="month" style="left:131px">JUN</span><span class="month" style="left:191px">SEP</span><span class="month" style="left:231px">NOV</span><span class="month" style="left:251.5px">DEZ</span>
    <i class="dot" style="left:31px"></i><i class="dot" style="left:72px"></i><i class="ring" style="left:92px"></i><i class="ring" style="left:131px"></i><i class="dot" style="left:191px"></i><i class="ring" style="left:231px"></i><i class="ring" style="left:251.5px"></i>
  </div>

  <div class="task-line" style="top:151px"></div><div class="task-label" style="top:147px">Task 1</div>
  <div class="task-line" style="top:167px"></div><div class="task-label" style="top:163px">Task 2</div>
  <div class="task-line" style="top:183.5px"></div><div class="task-label" style="top:179.5px">Task 3</div>
  <div class="task-line" style="top:200px"></div><div class="task-label" style="top:196px">Task 4</div>
  <div class="task-line" style="top:216.5px"></div><div class="task-label" style="top:212.5px">Task 5</div>
  <div class="task-line" style="top:233px"></div><div class="task-label" style="top:229px">Task 6</div>
  <div class="task-bar current" style="left:54.5px;width:40px;top:145.5px">Laserscanning</div>
  <div class="task-bar" style="left:69.5px;width:25px;top:161.5px">Drohne</div>
  <div class="task-bar" style="left:94.5px;width:183.5px;top:178px">Datenprozessierung</div>
  <div class="task-bar" style="left:133.5px;width:119.5px;top:194.5px">Datenbankmanagementsystem</div>
  <div class="task-bar" style="left:202.5px;width:50.5px;top:211px">3D-Modellierung</div>
  <div class="task-bar" style="left:275px;width:48px;top:227.5px">BIM-Viewer</div>

  <span class="play-mark" style="top:247px"></span>
</section>

<!-- Roadmap detail: paragraphs -->
<section class="slide" style="left:408px;top:330px">
  <h2 class="head-title" style="top:18px">Roadmap</h2>
  <div class="head-year" style="top:17px">2021</div>
  <div class="band" style="top:46px;height:198px"></div>
  <svg class="chev" style="left:21px;top:63px" viewBox="0 0 8 16"><polyline points="6.5,1 2,8 6.5,15" fill="none" stroke="#000" stroke-width="2.4"/></svg>
  <svg class="chev" style="left:316px;top:63px" viewBox="0 0 8 16"><polyline points="1.5,1 6,8 1.5,15" fill="none" stroke="#000" stroke-width="2.4"/></svg>
  <div class="track" style="top:64.5px">
    <span class="active"></span><span class="start"></span>
    <span class="month" style="left:31px">JAN</span><span class="month" style="left:72px">MAR</span><span class="month" style="left:92px">APR</span><span class="month" style="left:131px">JUN</span><span class="month" style="left:191px">SEP</span><span class="month" style="left:231px">NOV</span><span class="month" style="left:251.5px">DEZ</span>
    <i class="dot" style="left:31px"></i><i class="dot" style="left:72px"></i><i class="ring" style="left:92px"></i><i class="ring" style="left:131px"></i><i class="dot" style="left:191px"></i><i class="ring" style="left:231px"></i><i class="ring" style="left:251.5px"></i>
  </div>
  <div class="topic" style="top:92px">Laserscanning</div>
  <div class="gold-rule" style="left:56px;width:231px;top:108px"></div>
  <svg class="caret" style="top:115px" viewBox="0 0 18 6"><polyline points="1,1 9,5 17,1" fill="none" stroke="#333" stroke-width=".7"/></svg>
  <div class="card" style="top:124.5px;height:97px">
    <p class="para" style="top:13px">Maecenas sed diam dget risusu ipsum dolor sit amet, consectetur adipiscing elit ds. Nam suscipit felis sit amet nib Nam suscipit felis sit Maecenas sed</p>
    <p class="para" style="top:38.5px">Maecenas sed diam dget risusu ipsum dolor sit amet, consectetur adipiscing elit ds. Nam suscipit felis sit amet nib Nam suscipit felis sit Maecenas sed</p>
    <p class="para" style="top:64px">Maecenas sed diam dget risusu ipsum dolor sit amet, consectetur adipiscing elit ds. Nam suscipit felis sit amet nib Nam suscipit felis sit Maecenas sed</p>
  </div>
  <span class="play-mark" style="top:247px"></span>
</section>

<!-- Roadmap detail: bullets -->
<section class="slide" style="left:44px;top:608px">
  <h2 class="head-title" style="top:18px">Roadmap</h2>
  <div class="head-year" style="top:17px">2021</div>
  <div class="band" style="top:46px;height:198px"></div>
  <svg class="chev" style="left:21px;top:63px" viewBox="0 0 8 16"><polyline points="6.5,1 2,8 6.5,15" fill="none" stroke="#000" stroke-width="2.4"/></svg>
  <svg class="chev" style="left:316px;top:63px" viewBox="0 0 8 16"><polyline points="1.5,1 6,8 1.5,15" fill="none" stroke="#000" stroke-width="2.4"/></svg>
  <div class="track" style="top:64.5px">
    <span class="active"></span><span class="start"></span>
    <span class="month" style="left:31px">JAN</span><span class="month" style="left:72px">MAR</span><span class="month" style="left:92px">APR</span><span class="month" style="left:131px">JUN</span><span class="month" style="left:191px">SEP</span><span class="month" style="left:231px">NOV</span><span class="month" style="left:251.5px">DEZ</span>
    <i class="dot" style="left:31px"></i><i class="dot" style="left:72px"></i><i class="ring" style="left:92px"></i><i class="ring" style="left:131px"></i><i class="dot" style="left:191px"></i><i class="ring" style="left:231px"></i><i class="ring" style="left:251.5px"></i>
  </div>
  <div class="topic" style="top:92.5px">Laserscanning</div>
  <div class="gold-rule" style="left:56px;width:231px;top:108.5px"></div>
  <svg class="caret" style="top:116px" viewBox="0 0 18 6"><polyline points="1,1 9,5 17,1" fill="none" stroke="#333" stroke-width=".7"/></svg>
  <div class="card" style="top:124.5px;height:97.5px">
    <ul class="bullets" style="top:16px">
      <li>Maecenas sed diam dget risusu ipsum dolor sit amet, consectetur nsec</li>
      <li>Maecenas sed diam dget risusu ipsum dolor sit amet, consectetur nsec</li>
      <li>Maecenas sed diam dget risusu ipsum dolor sit amet, consectetur nsec</li>
      <li>Maecenas sed diam dget risusu ipsum dolor sit amet, consectetur nsec</li>
      <li>Maecenas sed diam dget risusu ipsum dolor sit amet, consectetur nsec</li>
    </ul>
  </div>
  <span class="play-mark" style="top:247px"></span>
</section>

<!-- Roadmap detail, timeline at bottom: paragraphs -->
<section class="slide" style="left:408px;top:608px">
  <div class="band" style="top:19px;height:197.5px"></div>
  <div class="card" style="top:31.5px;height:96.5px">
    <p class="para" style="top:14px">Maecenas sed diam dget risusu ipsum dolor sit amet, consectetur adipiscing elit ds. Nam suscipit felis sit amet nib Nam suscipit felis sit Maecenas sed</p>
    <p class="para" style="top:40px">Maecenas sed diam dget risusu ipsum dolor sit amet, consectetur adipiscing elit ds. Nam suscipit felis sit amet nib Nam suscipit felis sit Maecenas sed</p>
    <p class="para" style="top:65.5px">Maecenas sed diam dget risusu ipsum dolor sit amet, consectetur adipiscing elit ds. Nam suscipit felis sit amet nib Nam suscipit felis sit Maecenas sed</p>
  </div>
  <svg class="caret" style="top:136px" viewBox="0 0 18 6"><polyline points="1,5 9,1 17,5" fill="none" stroke="#333" stroke-width=".7"/></svg>
  <div class="gold-rule" style="left:56px;width:231px;top:151px"></div>
  <div class="topic" style="top:156.5px">Kick-off</div>
  <svg class="chev" style="left:21px;top:189px" viewBox="0 0 8 16"><polyline points="6.5,1 2,8 6.5,15" fill="none" stroke="#000" stroke-width="2.4"/></svg>
  <svg class="chev" style="left:316px;top:189px" viewBox="0 0 8 16"><polyline points="1.5,1 6,8 1.5,15" fill="none" stroke="#000" stroke-width="2.4"/></svg>
  <div class="track" style="top:190.5px">
    <span class="active"></span><span class="start"></span>
    <span class="month" style="left:31px">JAN</span><span class="month" style="left:72px">MAR</span><span class="month" style="left:92px">APR</span><span class="month" style="left:131px">JUN</span><span class="month" style="left:191px">SEP</span><span class="month" style="left:231px">NOV</span><span class="month" style="left:251.5px">DEZ</span>
    <i class="dot" style="left:31px"></i><i class="dot" style="left:72px"></i><i class="ring" style="left:92px"></i><i class="ring" style="left:131px"></i><i class="dot" style="left:191px"></i><i class="ring" style="left:231px"></i><i class="ring" style="left:251.5px"></i>
  </div>
  <h2 class="head-title" style="top:223px;left:20px">Roadmap</h2>
  <div class="head-year" style="top:226px">2021</div>
  <span class="play-mark" style="top:246px"></span>
</section>

<!-- Roadmap detail, timeline at bottom: bullets -->
<section class="slide" style="left:44px;top:885.5px">
  <div class="band" style="top:19px;height:197.5px"></div>
  <div class="card" style="top:32px;height:96.5px">
    <ul class="bullets" style="top:16px">
      <li>Maecenas sed diam dget risusu ipsum dolor sit amet, consectetur nsec</li>
      <li>Maecenas sed diam dget risusu ipsum dolor sit amet, consectetur nsec</li>
      <li>Maecenas sed diam dget risusu ipsum dolor sit amet, consectetur nsec</li>
      <li>Maecenas sed diam dget risusu ipsum dolor sit amet, consectetur nsec</li>
      <li>Maecenas sed diam dget risusu ipsum dolor sit amet, consectetur nsec</li>
    </ul>
  </div>
  <svg class="caret" style="top:137px" viewBox="0 0 18 6"><polyline points="1,5 9,1 17,5" fill="none" stroke="#333" stroke-width=".7"/></svg>
  <div class="gold-rule" style="left:56px;width:231px;top:151px"></div>
  <div class="topic" style="top:156.5px">Kick-off</div>
  <svg class="chev" style="left:21px;top:188px" viewBox="0 0 8 16"><polyline points="6.5,1 2,8 6.5,15" fill="none" stroke="#000" stroke-width="2.4"/></svg>
  <svg class="chev" style="left:316px;top:188px" viewBox="0 0 8 16"><polyline points="1.5,1 6,8 1.5,15" fill="none" stroke="#000" stroke-width="2.4"/></svg>
  <div class="track" style="top:189.5px">
    <span class="active"></span><span class="start"></span>
    <span class="month" style="left:31px">JAN</span><span class="month" style="left:72px">MAR</span><span class="month" style="left:92px">APR</span><span class="month" style="left:131px">JUN</span><span class="month" style="left:191px">SEP</span><span class="month" style="left:231px">NOV</span><span class="month" style="left:251.5px">DEZ</span>
    <i class="dot" style="left:31px"></i><i class="dot" style="left:72px"></i><i class="ring" style="left:92px"></i><i class="ring" style="left:131px"></i><i class="dot" style="left:191px"></i><i class="ring" style="left:231px"></i><i class="ring" style="left:251.5px"></i>
  </div>
  <h2 class="head-title" style="top:223px;left:20px">Roadmap</h2>
  <div class="head-year" style="top:226px">2021</div>
  <span class="play-mark" style="top:246px"></span>
</section>

<!-- Closing slide -->
<section class="slide" style="left:408px;top:885.5px;width:357px;height:267px">
  <div class="photo light" role="img" aria-label="Faded photo of a glass high-rise facade seen from below"></div>
  <h2 class="thanks-title">Thank You</h2>
  <div class="gold-rule" style="left:30px;top:91px;width:146px"></div>
  <div class="contact" style="top:113.5px">
    <span class="contact-icon"><svg width="8" height="9" viewBox="0 0 8 9"><path d="M4 8.6C2 6 1 4.6 1 3.3a3 3 0 0 1 6 0c0 1.3-1 2.7-3 5.3z" fill="#fff"/><circle cx="4" cy="3.3" r="1.1" fill="#000"/></svg></span>
    <span>214 Larkfield Rd, Nv, Usa</span>
  </div>
  <div class="contact" style="top:137px">
    <span class="contact-icon"><svg width="8" height="8" viewBox="0 0 8 8"><path d="M1.6.6l1.3 1.6-.8 1a4.6 4.6 0 0 0 1.8 1.8l1-.8 1.6 1.3-.8 1.3C3.6 6.7 1.3 4.4.3 1.4z" fill="#fff"/></svg></span>
    <span>(014) 672-3810</span>
  </div>
  <div class="contact" style="top:161px">
    <span class="contact-icon"></span>
    <span>https://Northpine.Com/</span>
  </div>
</section>

</body>
</html>
```